A start-up named "Corvath Therapeutics" - needs a new PowerPoint design

We need a new PowerPoint Design for an early-stage start-up named "Corvath Therapeutics" seeking to disrupt the current approach towards drug discovery within aging disorders.

We would like to build on Corvath's legacy, the founder of the modern science of genetics, by employing a multidisciplinary approach, experimenting, and providing elderly patients the attention they deserve.

We have selected the suffix "therapeutics" intentionally as it stands for (a medicine) the treatment of disease; the science of healing. Alzheimer’s treatment is a huge, urgent, unmet need:
- Shift from a disease-management system to a preventive medicine system
- Focus on increasing the health span, not only the life span

Target Market(s)

Pharma/ Biotech Executives Medical Institutions Healthcare professionals (MDs, nurses, payors, pharmacists, etc.) Patients

Industry/Entity Type

Healthcare

Other font styles liked:
• Celias

Colors
0054AA
0677BA
7BADD7
CADEEF
E8F1F8
E54698
E96AAD
F1A4CE
F9D9EA
FCEFF6
A7469A
B969AE
D3A5CF
EDDBEB
F8F0F9
6B429C
8869AF
B7A5CE
E3DAEB
F3F0F8

Requirements
Must have
• - differentiate from other companies named after Corvath - differentiate from other Pharma/ Biotech companies
Nice to have
• simplicity/ minimalist logo vivid colors gradient 3D Life-Sciences inspired Simple geometry Balance
Should not have
• mascot/ emblem watermark logo animated ink style nature-inspired inventive typography artistic chaos

```html
<!DOCTYPE html>
<html lang="en">
<head>
<meta charset="utf-8">
<title>Corvath Therapeutics – Presentation Design</title>
<link rel="stylesheet" href="https://fonts.googleapis.com/css2?family=Lexend:wght@300;400;500;600;700&display=swap">
<style>
:root{
  --magenta:#9c0b5f;
  --yellow:#f8ae1f;
  --plum:#5b0a3e;
  --orange:#d98a24;
  --black:#0f0f10;
  --grey:#9a9a9a;
  --ink:#333;
  --muted:#9a9a9a;
  --paper:#ffffff;
  --stage:#e2e2e6;
}
*{box-sizing:border-box;margin:0;padding:0}
html,body{width:1200px;height:2441px;overflow:hidden}
body{position:relative;background:var(--stage);font-family:"Lexend",sans-serif;color:var(--ink)}

/* ---------- hero ---------- */
.hero{position:absolute;left:0;top:0;width:1200px;height:790px;background:linear-gradient(180deg,#c7cad3 0%,#dcdde3 55%,#e2e2e6 100%)}
.hero-brand{position:absolute;left:930px;top:86px;display:flex;align-items:center;gap:12px}
.hero-brand .sq{width:20px;height:20px;background:var(--magenta)}
.hero-brand .name{font-size:40px;font-weight:500;color:var(--magenta);line-height:1}
.swatches{position:absolute;left:895px;top:182px;display:flex;gap:15px}
.swatches span{width:24px;height:24px;border-radius:50%}
.hero-slide{position:absolute;left:110px;top:190px;font-size:17.1px;box-shadow:0 18px 40px rgba(0,0,0,.18)}

/* ---------- title slide (em-based) ---------- */
.title-slide{position:relative;width:37.4em;height:21em;overflow:hidden;background:var(--paper)}
.title-slide .photo{position:absolute;right:0;top:0;width:62%;height:100%}
.title-slide svg.shape{position:absolute;inset:0;width:100%;height:100%}
.title-slide .brand{position:absolute;left:2.4em;top:3.6em;font-size:1.3em;font-weight:500;display:flex;align-items:center;gap:.35em}
.title-slide .brand i{width:.7em;height:.7em;background:currentColor;display:block}
.title-slide h1{position:absolute;left:1.2em;top:4.55em;font-size:2em;line-height:1.05;font-weight:600}
.title-slide h1 .b{color:var(--yellow)}
.title-slide .date{position:absolute;left:5.7em;top:33em;font-size:.42em}
.title-slide .copy{position:absolute;left:6.2em;top:48.5em;font-size:.38em;color:var(--muted)}
.t-white{color:var(--paper)}
.t-white .brand{color:var(--magenta)} .t-white h1 .a{color:var(--magenta)} .t-white .date{color:#222}
.t-black{color:var(--black)}
.t-black .brand,.t-black h1 .a,.t-black .date,.t-black .copy{color:#fff}
.t-mag{color:var(--magenta)}
.t-mag .brand,.t-mag h1 .a,.t-mag h1 .b,.t-mag .date,.t-mag .copy{color:#fff}
.ph-lab{background:linear-gradient(120deg,#cfd6dc,#e9eaea 40%,#b8c3cb 70%,#7d8f9f)}
.ph-sci{background:linear-gradient(120deg,#5b7690,#a9bccb 45%,#dfe6ec 70%,#6f8aa4)}
.ph-tab{background:linear-gradient(120deg,#8aa5bc,#c9d6e0 45%,#e8d7cf 65%,#7190ad)}

/* ---------- deck grid ---------- */
.deck{position:absolute;left:20px;top:812px;display:grid;grid-template-columns:repeat(3,374px);grid-auto-rows:210px;gap:19px}
.deck .title-slide{font-size:10px}
.slide{position:relative;width:374px;height:210px;background:var(--paper);overflow:hidden;font-size:4.4px;line-height:1.35;color:#777}
.slide h2{position:absolute;left:19px;top:15px;font-size:14px;font-weight:400;color:var(--magenta);line-height:1}
.slide h2 span{color:var(--yellow)}
.mark{position:absolute;right:18px;top:17px;font-size:7px;font-weight:500;color:var(--magenta);display:flex;align-items:center;gap:3px;line-height:1}
.mark i{width:6px;height:6px;background:var(--magenta);display:block}
.foot{position:absolute;left:6px;right:6px;bottom:5px;height:7px;border-radius:4px;background:linear-gradient(90deg,var(--magenta),var(--orange));color:#fff;font-size:3px;padding-left:6px;display:flex;align-items:center}
.foot b{position:absolute;right:6px;top:1px;height:5px;width:18px;border-radius:3px;background:var(--yellow);font-size:3px;text-align:center;line-height:5px;font-weight:400}
.ph{position:absolute}
.hm{color:var(--magenta);font-weight:500}
.hy{color:var(--yellow);font-weight:500}
.dark{color:#333;font-weight:500}

/* agenda */
.agenda{position:absolute;left:50px;top:62px;display:grid;grid-template-columns:148px 148px;row-gap:14px;column-gap:0}
.agenda .it{display:flex;gap:10px}
.agenda .n{font-size:14px;color:#ccc;font-weight:300;width:14px;line-height:1}
.agenda .it p:first-child{font-size:6px}

/* about */
.about h3{position:absolute;left:212px;top:63px;font-size:12px;font-weight:400;color:var(--yellow)}
.about .txt{position:absolute;left:212px;top:80px;width:140px}
ul.ticks{list-style:none}
ul.ticks li{position:relative;padding-left:5px;margin-top:2px}
ul.ticks li::before{content:"";position:absolute;left:0;top:1.3px;width:2px;height:2px;border-radius:50%;background:var(--magenta)}

/* team */
.team{position:absolute;left:0;right:0;top:58px;display:flex;justify-content:space-around;padding:0 26px}
.member{width:100px;text-align:center}
.member .av{width:48px;height:48px;border-radius:50%;margin:0 auto 6px;background:radial-gradient(circle at 50% 40%,#c9b8a8,#6f6a6a 70%,#48505a)}
.member .nm{font-size:6px}

/* icon row */
.icons{position:absolute;left:28px;right:28px;top:96px;display:flex;justify-content:space-between}
.icons .c{width:72px;text-align:center}
.icons .dot{width:22px;height:22px;border-radius:50%;margin:0 auto 5px;display:flex;align-items:center;justify-content:center}
.icons .h{font-size:6px;margin-bottom:2px}

/* columns */
.cols{position:absolute;left:20px;right:20px;top:58px;display:grid;grid-template-columns:repeat(3,1fr);gap:0}
.cols > div{padding:0 8px;border-left:1px solid #eee}
.cols > div:first-child{border-left:0;padding-left:2px}
.cols h4{font-size:6px;font-weight:500;color:var(--magenta);margin-bottom:6px}
.cols > div:nth-child(2) h4{color:var(--yellow)}

/* timeline */
.tl{position:absolute;left:24px;right:24px;top:113px;display:flex;justify-content:space-between}
.tl .st{width:40px;position:relative;text-align:center}
.tl .num{width:16px;height:16px;border-radius:50%;color:#fff;font-size:7px;line-height:16px;margin:0 auto}
.tl .lab{position:absolute;left:-6px;right:-6px;font-size:5px;line-height:1.1;text-align:center}
.tl .up{bottom:22px}
.tl .dn{top:22px}
.tl .note{position:absolute;left:2px;width:44px;text-align:left}

/* table */
.tbl{position:absolute;left:26px;top:60px;width:324px;border-collapse:collapse;font-size:3.8px;color:#333}
.tbl th{height:10px;font-weight:400;color:#fff;font-size:4px}
.tbl td{height:8px;border-bottom:1px solid #eee;text-align:center}
.tbl td:first-child{text-align:left;padding-left:2px}

/* quote */
.quote{position:absolute;top:66px;width:108px;height:120px;padding:10px 10px;color:#fff;font-size:5.5px;line-height:1.3}
.quote .qm{font-size:20px;font-weight:700;line-height:.8;display:block;margin-bottom:8px}

/* contact */
.contact{position:relative;width:374px;height:210px;overflow:hidden;color:#fff}
.contact .bg{position:absolute;inset:0}
.contact .brand{position:absolute;left:36px;top:79px;font-size:13px;font-weight:500;display:flex;gap:5px;align-items:center}
.contact .brand i{width:8px;height:8px;background:#fff;display:block}
.contact h3{position:absolute;left:36px;top:117px;font-size:10px;font-weight:400}
.contact .addr{position:absolute;left:36px;top:133px;font-size:5px}
.contact ul{position:absolute;left:36px;top:146px;list-style:none;font-size:5px}
.contact li{display:flex;align-items:center;gap:5px;margin-bottom:3px}
.contact .copy{position:absolute;left:140px;top:196px;font-size:3.5px;opacity:.8}
</style>
</head>
<body>

<section class="hero">
  <div class="hero-slide">
    <div class="title-slide t-white">
      <div class="photo ph-lab" role="img" aria-label="Photo of a masked lab researcher reviewing documents in a pharmacy"></div>
      <svg class="shape" viewBox="0 0 374 210" preserveAspectRatio="none" aria-hidden="true">
        <polygon points="250,0 300,0 374,80 374,140" fill="#9c0b5f" opacity=".35"/>
        <polygon points="105,0 170,0 262,105 230,105" fill="#f8ae1f"/>
        <polygon points="200,140 232,105 340,210 272,210" fill="#9c0b5f" opacity=".85"/>
        <polygon points="0,0 120,0 232,105 120,210 0,210" fill="currentColor"/>
      </svg>
      <div class="brand"><i></i>Corvath</div>
      <h1><span class="a">Corvath</span><br><span class="b">Therapeutics</span></h1>
      <p class="date">Monday, January 17, 2022</p>
      <p class="copy">© 2021 Corvath Therapeutics, All Rights Reserved.</p>
    </div>
  </div>
  <div class="hero-brand"><span class="sq"></span><span class="name">Corvath</span></div>
  <div class="swatches">
    <span style="background:var(--magenta)"></span>
    <span style="background:var(--yellow)"></span>
    <span style="background:var(--plum)"></span>
    <span style="background:var(--orange)"></span>
    <span style="background:var(--black)"></span>
    <span style="background:var(--grey)"></span>
  </div>
</section>

<main class="deck">

  <!-- title slides -->
  <div class="title-slide t-white">
    <div class="photo ph-lab" role="img" aria-label="Photo of a masked lab researcher in a pharmacy"></div>
    <svg class="shape" viewBox="0 0 374 210" preserveAspectRatio="none" aria-hidden="true"><polygon points="250,0 300,0 374,80 374,140" fill="#9c0b5f" opacity=".35"/><polygon points="105,0 170,0 262,105 230,105" fill="#f8ae1f"/><polygon points="200,140 232,105 340,210 272,210" fill="#9c0b5f" opacity=".85"/><polygon points="0,0 120,0 232,105 120,210 0,210" fill="currentColor"/></svg>
    <div class="brand"><i></i>Corvath</div>
    <h1><span class="a">Corvath</span><br><span class="b">Therapeutics</span></h1>
    <p class="date">Monday, January 17, 2022</p>
    <p class="copy">© 2021 Corvath Therapeutics, All Rights Reserved.</p>
  </div>
  <div class="title-slide t-black">
    <div class="photo ph-sci" role="img" aria-label="Photo of a scientist working with samples in a laboratory"></div>
    <svg class="shape" viewBox="0 0 374 210" preserveAspectRatio="none" aria-hidden="true"><polygon points="250,0 300,0 374,80 374,140" fill="#9c0b5f" opacity=".35"/><polygon points="105,0 170,0 262,105 230,105" fill="#f8ae1f"/><polygon points="200,140 232,105 340,210 272,210" fill="#9c0b5f" opacity=".85"/><polygon points="0,0 120,0 232,105 120,210 0,210" fill="currentColor"/></svg>
    <div class="brand"><i></i>Corvath</div>
    <h1><span class="a">Corvath</span><br><span class="b">Therapeutics</span></h1>
    <p class="date">Monday, January 17, 2022</p>
    <p class="copy">© 2021 Corvath Therapeutics, All Rights Reserved.</p>
  </div>
  <div class="title-slide t-mag">
    <div class="photo ph-tab" role="img" aria-label="Photo of hands using a tablet"></div>
    <svg class="shape" viewBox="0 0 374 210" preserveAspectRatio="none" aria-hidden="true"><polygon points="250,0 300,0 374,80 374,140" fill="#9c0b5f" opacity=".35"/><polygon points="105,0 170,0 262,105 230,105" fill="#f8ae1f"/><polygon points="200,140 232,105 340,210 272,210" fill="#9c0b5f" opacity=".85"/><polygon points="0,0 120,0 232,105 120,210 0,210" fill="currentColor"/></svg>
    <div class="brand"><i></i>Corvath</div>
    <h1><span class="a">Corvath</span><br><span class="b">Therapeutics</span></h1>
    <p class="date">Monday, January 17, 2022</p>
    <p class="copy">© 2021 Corvath Therapeutics, All Rights Reserved.</p>
  </div>
  <div class="title-slide t-white">
    <div class="photo ph-lab" role="img" aria-label="Photo of a masked lab researcher in a pharmacy"></div>
    <svg class="shape" viewBox="0 0 374 210" preserveAspectRatio="none" aria-hidden="true"><polygon points="250,0 300,0 374,80 374,140" fill="#9c0b5f" opacity=".35"/><polygon points="105,0 170,0 262,105 230,105" fill="#f8ae1f"/><polygon points="200,140 232,105 340,210 272,210" fill="#9c0b5f" opacity=".85"/><polygon points="0,0 120,0 232,105 120,210 0,210" fill="currentColor"/></svg>
    <div class="brand"><i></i>Corvath</div>
    <h1><span class="a">Corvath</span><br><span class="b">Therapeutics</span></h1>
    <p class="date">Monday, January 17, 2022</p>
    <p class="copy">© 2021 Corvath Therapeutics, All Rights Reserved.</p>
  </div>
  <div class="title-slide t-black">
    <div class="photo ph-sci" role="img" aria-label="Photo of a scientist working with samples in a laboratory"></div>
    <svg class="shape" viewBox="0 0 374 210" preserveAspectRatio="none" aria-hidden="true"><polygon points="250,0 300,0 374,80 374,140" fill="#9c0b5f" opacity=".35"/><polygon points="105,0 170,0 262,105 230,105" fill="#f8ae1f"/><polygon points="200,140 232,105 340,210 272,210" fill="#9c0b5f" opacity=".85"/><polygon points="0,0 120,0 232,105 120,210 0,210" fill="currentColor"/></svg>
    <div class="brand"><i></i>Corvath</div>
    <h1><span class="a">Corvath</span><br><span class="b">Therapeutics</span></h1>
    <p class="date">Monday, January 17, 2022</p>
    <p class="copy">© 2021 Corvath Therapeutics, All Rights Reserved.</p>
  </div>
  <div class="title-slide t-mag">
    <div class="photo ph-tab" role="img" aria-label="Photo of hands using a tablet"></div>
    <svg class="shape" viewBox="0 0 374 210" preserveAspectRatio="none" aria-hidden="true"><polygon points="250,0 300,0 374,80 374,140" fill="#9c0b5f" opacity=".35"/><polygon points="105,0 170,0 262,105 230,105" fill="#f8ae1f"/><polygon points="200,140 232,105 340,210 272,210" fill="#9c0b5f" opacity=".85"/><polygon points="0,0 120,0 232,105 120,210 0,210" fill="currentColor"/></svg>
    <div class="brand"><i></i>Corvath</div>
    <h1><span class="a">Corvath</span><br><span class="b">Therapeutics</span></h1>
    <p class="date">Monday, January 17, 2022</p>
    <p class="copy">© 2021 Corvath Therapeutics, All Rights Reserved.</p>
  </div>

  <!-- agenda -->
  <div class="slide">
    <h2>Agenda <span>Slide</span></h2>
    <div class="mark"><i></i>Corvath</div>
    <div class="agenda">
      <div class="it"><span class="n">1</span><div><p class="hm">Title Goes Here</p><p>Short note on this topic.<br>Key point goes here.</p></div></div>
      <div class="it"><span class="n">2</span><div><p class="hy">Title Goes Here</p><p>Short note on this topic.<br>Key point goes here.</p></div></div>
      <div class="it"><span class="n">3</span><div><p class="hy">Title Goes Here</p><p>Short note on this topic.<br>Key point goes here.</p></div></div>
      <div class="it"><span class="n">4</span><div><p class="hm">Title Goes Here</p><p>Short note on this topic.<br>Key point goes here.</p></div></div>
      <div class="it"><span class="n">5</span><div><p class="hm">Title Goes Here</p><p>Short note on this topic.<br>Key point goes here.</p></div></div>
      <div class="it"><span class="n">6</span><div><p class="hy">Title Goes Here</p><p>Short note on this topic.<br>Key point goes here.</p></div></div>
    </div>
    <div class="foot">© 2021 Corvath Therapeutics, All Rights Reserved.<b>7</b></div>
  </div>

  <!-- about -->
  <div class="slide about">
    <div class="mark"><i></i>Corvath</div>
    <div class="ph ph-sci" style="left:24px;top:0;width:174px;height:112px" role="img" aria-label="Photo of a scientist in a laboratory"></div>
    <div class="ph ph-tab" style="left:24px;top:117px;width:83px;height:57px" role="img" aria-label="Photo of hands holding a tablet"></div>
    <div class="ph ph-lab" style="left:112px;top:117px;width:86px;height:57px" role="img" aria-label="Photo of a researcher in a pharmacy"></div>
    <h3>About Us</h3>
    <div class="txt">
      <p>We study aging disorders with a multidisciplinary team, testing new ideas and caring for elderly patients.</p>
      <ul class="ticks">
        <li>Preventive care over disease management.</li>
        <li>Health span matters, not only life span.</li>
        <li>Early research focused on memory loss and its causes in later life.</li>
        <li>Open work with clinics and partners.</li>
      </ul>
    </div>
    <div class="foot">© 2021 Corvath Therapeutics, All Rights Reserved.<b>8</b></div>
  </div>

  <!-- team -->
  <div class="slide">
    <h2>Meet Our <span>Team</span></h2>
    <div class="mark"><i></i>Corvath</div>
    <div class="team">
      <div class="member"><div class="av" role="img" aria-label="Team member portrait"></div><p class="nm hm">Name Goes Here</p><p>Job Title Goes Here</p><p>A short line about this person and their role on the team.</p></div>
      <div class="member"><div class="av" role="img" aria-label="Team member portrait"></div><p class="nm hy">Name Goes Here</p><p>Job Title Goes Here</p><p>A short line about this person and their role on the team.</p></div>
      <div class="member"><div class="av" role="img" aria-label="Team member portrait"></div><p class="nm dark">Name Goes Here</p><p>Job Title Goes Here</p><p>A short line about this person and their role on the team.</p></div>
    </div>
    <div class="foot">© 2021 Corvath Therapeutics, All Rights Reserved.<b>9</b></div>
  </div>

  <!-- bullets + band -->
  <div class="slide">
    <h2>Slide Title <span>Goes Here</span></h2>
    <div class="mark"><i></i>Corvath</div>
    <ul class="ticks" style="position:absolute;left:19px;top:38px;width:180px">
      <li>Our approach joins biology, data and care to find new paths in aging research.</li>
      <li>We run small, fast studies and share what we learn with partner clinics and labs.</li>
      <li>Patients and families help shape every study from the first day onward.</li>
    </ul>
    <div class="ph ph-sci" style="left:210px;top:38px;width:134px;height:80px" role="img" aria-label="Photo of a scientist at a microscope"></div>
    <div style="position:absolute;left:0;right:0;top:100px;height:55px;background:linear-gradient(90deg,var(--magenta) 60%,var(--yellow));color:#fff;font-size:5px;padding:9px 112px 0 38px">Our work aims to move care from treating disease to preventing it, so that people live longer in good health. Each program starts with a clear need and a clear test, and we keep patients at the heart of every step we take.</div>
    <div class="foot">© 2021 Corvath Therapeutics, All Rights Reserved.<b>10</b></div>
  </div>

  <!-- icons -->
  <div class="slide">
    <h2>Slide Title <span>Goes Here</span></h2>
    <div class="mark"><i></i>Corvath</div>
    <p style="position:absolute;left:26px;right:26px;top:50px;text-align:center">A short intro line sits here to frame the four ideas below and lead the reader into the points on this slide.</p>
    <div class="icons">
      <div class="c"><div class="dot" style="background:var(--magenta)"><svg width="12" height="12" viewBox="0 0 12 12"><path d="M1 3l4 3-4 3M11 3L7 6l4 3" stroke="#fff" fill="none" stroke-width="1.2"/></svg></div><p class="h hm">Heading</p><p>Brief text for this point goes here in a few lines.</p></div>
      <div class="c"><div class="dot" style="background:var(--yellow)"><svg width="12" height="12" viewBox="0 0 12 12"><path d="M2 6h8a4 4 0 0 1-8 0z" fill="#fff"/></svg></div><p class="h hy">Heading</p><p>Brief text for this point goes here in a few lines.</p></div>
      <div class="c"><div class="dot" style="background:var(--plum)"><svg width="12" height="12" viewBox="0 0 12 12"><circle cx="6" cy="5" r="2.5" fill="none" stroke="#fff"/><path d="M3 10h6" stroke="#fff"/></svg></div><p class="h" style="color:var(--plum);font-weight:500">Heading</p><p>Brief text for this point goes here in a few lines.</p></div>
      <div class="c"><div class="dot" style="background:var(--orange)"><svg width="12" height="12" viewBox="0 0 12 12"><path d="M4.5 2h3v3l2.5 5h-8L4.5 5z" fill="#fff"/></svg></div><p class="h" style="color:var(--orange);font-weight:500">Heading</p><p>Brief text for this point goes here in a few lines.</p></div>
    </div>
    <div class="foot">© 2021 Corvath Therapeutics, All Rights Reserved.<b>11</b></div>
  </div>

  <!-- photo strip -->
  <div class="slide">
    <h2>Slide Title <span>Goes Here</span></h2>
    <div class="mark"><i></i>Corvath</div>
    <p style="position:absolute;left:19px;right:19px;top:38px">We bring lab science and clinical care together to study how the brain ages and how we can slow decline. Our teams test ideas early, learn fast and share results with partners. Each program is built around one clear question and the people who live with the condition every day.</p>
    <div class="ph ph-sci" style="left:0;top:97px;width:200px;height:75px" role="img" aria-label="Photo of a microscope and sample trays in a lab"></div>
    <div style="position:absolute;left:192px;top:97px;width:160px;height:75px;background:linear-gradient(90deg,var(--magenta),#c3503f 70%,var(--orange));color:#fff;font-size:8px;line-height:1.25;padding:11px 10px">A short quote sits here in this box to pull out a key idea from the slide above.</div>
    <div class="foot">© 2021 Corvath Therapeutics, All Rights Reserved.<b>12</b></div>
  </div>

  <!-- three columns -->
  <div class="slide">
    <h2>Slide Title <span>Goes Here</span></h2>
    <div class="mark"><i></i>Corvath</div>
    <div class="cols">
      <div><h4>Title Goes Here!</h4><ul class="ticks"><li>Short line on this idea that runs over a few lines of text.</li><li>A second point with a little more detail for the reader.</li><li>A third point to close.</li><li>One more short note.</li></ul></div>
      <div><h4>Title Goes Here!</h4><ul class="ticks"><li>Short line on this idea that runs over a few lines of text.</li><li>A second point with a little more detail for the reader.</li><li>A third point to close.</li><li>One more short note.</li></ul></div>
      <div><h4 style="color:#333">Title Goes Here!</h4><ul class="ticks"><li>Short line on this idea that runs over a few lines of text.</li><li>A second point with a little more detail for the reader.</li><li>A third point to close.</li><li>One more short note.</li></ul></div>
    </div>
    <div class="foot">© 2021 Corvath Therapeutics, All Rights Reserved.<b>13</b></div>
  </div>

  <!-- timeline -->
  <div class="slide">
    <h2>Slide Title <span>Goes Here</span></h2>
    <div class="mark"><i></i>Corvath</div>
    <div class="tl">
      <div class="st"><div class="num" style="background:var(--magenta)">1</div><p class="lab up hm">Heading<br>Goes Here!</p><p class="lab dn" style="top:48px">✓ Short step note here.</p></div>
      <div class="st"><p class="lab up" style="bottom:24px">✓ Short step note here.<br><br><span class="hy">Heading<br>Goes Here!</span></p><div class="num" style="background:var(--yellow)">2</div></div>
      <div class="st"><div class="num" style="background:var(--plum)">3</div><p class="lab dn" style="color:var(--plum);font-weight:500">Heading<br>Goes Here!</p><p class="lab dn" style="top:40px">✓ Short step note here.</p></div>
      <div class="st"><p class="lab up" style="bottom:24px">✓ Short step note here.<br><br><span style="color:var(--orange);font-weight:500">Heading<br>Goes Here!</span></p><div class="num" style="background:var(--orange)">4</div></div>
      <div class="st"><div class="num" style="background:var(--black)">5</div><p class="lab dn dark">Heading<br>Goes Here!</p><p class="lab dn" style="top:40px">✓ Short step note here.</p></div>
      <div class="st"><p class="lab up" style="bottom:24px">✓ Short step note here.<br><br><span style="color:var(--grey)">Heading<br>Goes Here!</span></p><div class="num" style="background:var(--grey)">6</div></div>
    </div>
    <div class="foot">© 2021 Corvath Therapeutics, All Rights Reserved.<b>14</b></div>
  </div>

  <!-- column chart -->
  <div class="slide">
    <h2>Column <span>Chart Slide</span></h2>
    <div class="mark"><i></i>Corvath</div>
    <svg style="position:absolute;left:18px;top:60px" width="200" height="110" viewBox="0 0 200 110" aria-label="Column chart with four categories and three series">
      <g font-size="4" fill="#777" font-family="Lexend,sans-serif">
        <text x="2" y="6">6</text><text x="2" y="21">5</text><text x="2" y="36">4</text><text x="2" y="51">3</text><text x="2" y="66">2</text><text x="2" y="81">1</text><text x="2" y="96">0</text>
      </g>
      <line x1="10" y1="95" x2="195" y2="95" stroke="#ddd" stroke-width=".6"/>
      <g>
        <rect x="22" y="30" width="7" height="65" fill="#9c0b5f"/><rect x="30" y="63" width="7" height="32" fill="#f8ae1f"/><rect x="38" y="56" width="7" height="39" fill="#5b0a3e"/>
        <rect x="67" y="60" width="7" height="35" fill="#9c0b5f"/><rect x="75" y="29" width="7" height="66" fill="#f8ae1f"/><rect x="83" y="62" width="7" height="33" fill="#5b0a3e"/>
        <rect x="112" y="43" width="7" height="52" fill="#9c0b5f"/><rect x="120" y="67" width="7" height="28" fill="#f8ae1f"/><rect x="128" y="51" width="7" height="44" fill="#5b0a3e"/>
        <rect x="157" y="30" width="7" height="65" fill="#9c0b5f"/><rect x="165" y="54" width="7" height="41" fill="#f8ae1f"/><rect x="173" y="20" width="7" height="75" fill="#5b0a3e"/>
      </g>
      <g font-size="3.5" fill="#555" font-family="Lexend,sans-serif" text-anchor="middle">
        <text x="33" y="101">Category 1</text><text x="78" y="101">Category 2</text><text x="123" y="101">Category 3</text><text x="168" y="101">Category 4</text>
        <text x="100" y="108">■ Series 1  ■ Series 2  ■ Series 3</text>
      </g>
    </svg>
    <div style="position:absolute;left:240px;top:63px;width:115px">
      <p class="hm" style="font-size:5.5px"><span style="display:inline-block;width:5px;height:5px;background:var(--magenta);margin-right:4px"></span>Title Goes Here!</p>
      <p style="padding-left:9px;margin-bottom:12px">A short note on this series and what the numbers show.</p>
      <p class="hy" style="font-size:5.5px"><span style="display:inline-block;width:5px;height:5px;background:var(--yellow);margin-right:4px"></span>Title Goes Here!</p>
      <p style="padding-left:9px;margin-bottom:12px">A short note on this series and what the numbers show.</p>
      <p style="font-size:5.5px;color:var(--plum);font-weight:500"><span style="display:inline-block;width:5px;height:5px;background:var(--plum);margin-right:4px"></span>Title Goes Here!</p>
      <p style="padding-left:9px">A short note on this series and what the numbers show.</p>
    </div>
    <div class="foot">© 2021 Corvath Therapeutics, All Rights Reserved.<b>15</b></div>
  </div>

  <!-- pie chart -->
  <div class="slide">
    <h2>Pie <span>Chart Slide</span></h2>
    <div class="mark"><i></i>Corvath</div>
    <div style="position:absolute;left:0;right:0;top:64px;height:104px;background:#f5f5f5"></div>
    <div style="position:absolute;left:0;top:64px;width:14px;height:48px;background:var(--yellow)"></div>
    <div style="position:absolute;left:0;top:115px;width:14px;height:53px;background:var(--magenta)"></div>
    <div style="position:absolute;right:0;top:64px;width:14px;height:48px;background:var(--magenta)"></div>
    <div style="position:absolute;right:0;top:115px;width:14px;height:53px;background:var(--yellow)"></div>
    <svg style="position:absolute;left:0;top:64px" width="374" height="104" aria-label="Pie chart with four segments">
      <g font-size="7" fill="#fff" font-family="Lexend,sans-serif" text-anchor="middle">
        <text transform="translate(10 88) rotate(-90)">20%</text><text transform="translate(10 140) rotate(-90)" x="-52" >40%</text>
        <text transform="translate(367 88) rotate(-90)">80%</text><text transform="translate(367 140) rotate(-90)" x="-52">60%</text>
      </g>
      <g transform="translate(187 52)">
        <path d="M0 0L0-56A56 56 0 0 1 17.3 53.3Z" fill="#9c0b5f"/>
        <path d="M0 0L17.3 53.3A56 56 0 0 1-56 0Z" fill="#f8ae1f"/>
        <path d="M0 0L-56 0A56 56 0 0 1-32.9-45.3Z" fill="#5b0a3e"/>
        <path d="M0 0L-32.9-45.3A56 56 0 0 1 0-56Z" fill="#d98a24"/>
        <g font-size="5" fill="#fff" font-family="Lexend,sans-serif" text-anchor="middle">
          <text x="42" y="-10">80%</text><text x="-15" y="48">60%</text><text x="-42" y="-12">40%</text><text x="-14" y="-46">20%</text>
        </g>
      </g>
    </svg>
    <div style="position:absolute;left:34px;top:78px;width:90px;text-align:center"><p class="hy" style="font-size:6px">Heading</p><p>Short note for this slice of the chart.</p></div>
    <div style="position:absolute;left:34px;top:128px;width:90px;text-align:center"><p class="hm" style="font-size:6px">Heading</p><p>Short note for this slice of the chart.</p></div>
    <div style="position:absolute;right:34px;top:78px;width:90px;text-align:center"><p class="hm" style="font-size:6px">Heading</p><p>Short note for this slice of the chart.</p></div>
    <div style="position:absolute;right:34px;top:128px;width:90px;text-align:center"><p class="hy" style="font-size:6px">Heading</p><p>Short note for this slice of the chart.</p></div>
    <div class="foot">© 2021 Corvath Therapeutics, All Rights Reserved.<b>16</b></div>
  </div>

  <!-- table -->
  <div class="slide">
    <h2 style="color:var(--magenta)">Table <span>Slide</span></h2>
    <div class="mark"><i></i>Corvath</div>
    <table class="tbl">
      <tr>
        <th rowspan="3" style="background:var(--magenta);font-size:10px;text-align:left;padding-left:4px;line-height:1.05;width:80px">Title Goes<br>Here!</th>
        <th style="background:var(--yellow)">Heading 1</th><th style="background:var(--magenta)">Heading 2</th><th style="background:var(--orange)">Heading 3</th>
      </tr>
      <tr><th style="background:var(--yellow);font-size:10px">2019</th><th style="background:var(--magenta);font-size:10px">2020</th><th style="background:var(--orange);font-size:10px">2021</th></tr>
      <tr><th style="background:#fbc55a;height:7px;font-size:3px">Text Goes Here</th><th style="background:#b6337e;height:7px;font-size:3px">Text Goes Here</th><th style="background:#e6a349;height:7px;font-size:3px">Text Goes Here</th></tr>
      <tr><td>Text Goes Here</td><td style="color:var(--yellow)">✓</td><td>✓</td><td style="color:var(--orange)">✓</td></tr>
      <tr><td>Text Goes Here</td><td style="color:var(--yellow)">✓</td><td>✓</td><td style="color:var(--orange)">✓</td></tr>
      <tr><td>Text Goes Here</td><td style="color:var(--yellow)">✓</td><td></td><td style="color:var(--orange)">✓</td></tr>
      <tr><td>Text Goes Here</td><td></td><td>✓</td><td style="color:var(--orange)">✓</td></tr>
      <tr><td>Text Goes Here</td><td style="color:var(--yellow)">✓</td><td></td><td style="color:var(--orange)">✓</td></tr>
      <tr><th style="background:var(--magenta);height:7px"></th><th style="background:var(--yellow);height:7px;font-size:3px">Text Goes Here</th><th style="background:var(--magenta);height:7px;font-size:3px">Text Goes Here</th><th style="background:var(--orange);height:7px;font-size:3px">Text Goes Here</th></tr>
    </table>
    <div class="foot">© 2021 Corvath Therapeutics, All Rights Reserved.<b>17</b></div>
  </div>

  <!-- quotes -->
  <div class="slide">
    <h2>Slide Title <span>Goes Here</span></h2>
    <div class="mark"><i></i>Corvath</div>
    <div class="ph ph-tab" style="left:0;top:66px;width:124px;height:120px" role="img" aria-label="Photo of hands using a tablet"></div>
    <div class="quote" style="left:132px;background:var(--magenta)"><span class="qm">“</span>A short quote from a partner or patient sits here, sharing why this work matters to them and to the people they care for each day.</div>
    <div class="quote" style="left:248px;background:var(--yellow)"><span class="qm">“</span>A short quote from a partner or patient sits here, sharing why this work matters to them and to the people they care for each day.</div>
    <div class="foot">© 2021 Corvath Therapeutics, All Rights Reserved.<b>18</b></div>
  </div>

  <!-- contact slides -->
  <div class="contact">
    <div class="bg" role="img" aria-label="Dark city building photo with magenta tint" style="background:linear-gradient(120deg,#1a0612,#4a1038 55%,#9c0b5f 80%,#6d2050)"></div>
    <svg style="position:absolute;inset:0" width="374" height="210" aria-hidden="true"><polygon points="170,0 230,0 330,100 300,130" fill="#f8ae1f" opacity=".8"/><polygon points="120,0 170,0 300,130 250,180" fill="#9c0b5f" opacity=".35"/></svg>
    <div class="brand"><i></i>Corvath</div>
    <h3>Contact Us</h3>
    <p class="addr">Insert Company Address Here!</p>
    <ul><li>☎ Insert Phone Number</li><li>@ Insert E-Mail Address</li><li>◎ Insert URL Address</li></ul>
    <p class="copy">© 2021 Corvath Therapeutics, All Rights Reserved.</p>
  </div>
  <div class="contact">
    <div class="bg" role="img" aria-label="Dark city building photo with gold tint" style="background:linear-gradient(120deg,#120d05,#4a3a14 55%,#8a6a22 80%,#5a4a28)"></div>
    <svg style="position:absolute;inset:0" width="374" height="210" aria-hidden="true"><polygon points="170,0 230,0 330,100 300,130" fill="#9c0b5f" opacity=".8"/><polygon points="120,0 170,0 300,130 250,180" fill="#f8ae1f" opacity=".3"/></svg>
    <div class="brand"><i></i>Corvath</div>
    <h3>Contact Us</h3>
    <p class="addr">Insert Company Address Here!</p>
    <ul><li>☎ Insert Phone Number</li><li>@ Insert E-Mail Address</li><li>◎ Insert URL Address</li></ul>
    <p class="copy">© 2021 Corvath Therapeutics, All Rights Reserved.</p>
  </div>
  <div class="contact">
    <div class="bg" role="img" aria-label="Dark city building photo in greyscale" style="background:linear-gradient(120deg,#0c0c0c,#2a2a2a 55%,#555 80%,#3a3a3a)"></div>
    <svg style="position:absolute;inset:0" width="374" height="210" aria-hidden="true"><polygon points="170,0 230,0 330,100 300,130" fill="#f8ae1f" opacity=".8"/><polygon points="120,0 170,0 300,130 250,180" fill="#9c0b5f" opacity=".35"/></svg>
    <div class="brand"><i></i>Corvath</div>
    <h3>Contact Us</h3>
    <p class="addr">Insert Company Address Here!</p>
    <ul><li>☎ Insert Phone Number</li><li>@ Insert E-Mail Address</li><li>◎ Insert URL Address</li></ul>
    <p class="copy">© 2021 Corvath Therapeutics, All Rights Reserved.</p>
  </div>

</main>
</body>
</html>
```